ORB Stationary and Biz cards
Please include the logo I have attached.
Simple
Dorotea Wellmont
dpalvane@qzr.example
www.orbworthkeeping.example
Hello,
I will provide the proper address in a few days. It will take one line for address and one for city and state.
I uploaded the entire file of my logo, not only the AI format. Please let me know if this is a problem. Thank you!
Please let me know if you cannot access the subfiles within this file for your use. Thanks!
Please let me know if you have problems opening the AI file in this attachment. Thank you!
ORB

```html
<!DOCTYPE html>
<html lang="en">
<head>
<meta charset="utf-8">
<title>ORB Business Card</title>
<link rel="stylesheet" href="https://fonts.googleapis.com/css2?family=Open+Sans:wght@400;600;700&display=swap">
<style>
  :root {
    --page: #e9ebee;
    --card: #ffffff;
    --blue-deep: #1561b8;
    --blue-mid: #2a85d6;
    --blue-light: #4aa8ea;
    --green: #6cc04a;
    --white: #ffffff;
    --ink-blue: #1f6fc4;
  }
  * { margin: 0; padding: 0; box-sizing: border-box; }
  html, body {
    width: 1200px; height: 914px; overflow: hidden;
    background: var(--page);
    font-family: "Open Sans", Arial, sans-serif;
  }
  .business-card {
    position: absolute; left: 100px; top: 167px;
    width: 1000px; height: 580px;
    background: var(--card);
    box-shadow: 0 12px 30px rgba(0,0,0,0.18);
    overflow: hidden;
  }
  .card-shapes { position: absolute; inset: 0; width: 100%; height: 100%; }
  .holder { position: absolute; left: 62px; top: 44px; color: var(--white); }
  .holder-name { font-size: 24px; font-weight: 700; letter-spacing: 0.2px; }
  .holder-role { font-size: 18px; font-weight: 400; margin-top: 4px; opacity: 0.95; }
  .contact-list {
    position: absolute; left: 62px; top: 322px;
    list-style: none; color: var(--white);
    font-size: 17px; line-height: 1.25;
  }
  .contact-item { display: flex; align-items: flex-start; gap: 12px; margin-bottom: 9px; }
  .contact-icon {
    flex: none; width: 22px; height: 22px; border-radius: 50%;
    background: var(--white); display: flex; align-items: center; justify-content: center;
  }
  .contact-icon svg { width: 13px; height: 13px; fill: var(--blue-mid); }
  .brand {
    position: absolute; left: 700px; top: 232px;
    display: flex; align-items: center; gap: 18px;
  }
  .brand-square { width: 34px; height: 34px; background: var(--green); }
  .brand-name {
    font-size: 96px; font-weight: 700; color: var(--ink-blue);
    line-height: 1; letter-spacing: 2px;
  }
</style>
</head>
<body>
  <div class="business-card">
    <svg class="card-shapes" viewBox="0 0 1000 580" preserveAspectRatio="none" aria-hidden="true">
      <defs>
        <radialGradient id="panelGlow" cx="0.35" cy="0.45" r="0.75">
          <stop offset="0" stop-color="#4aa8ea"/>
          <stop offset="0.6" stop-color="#2a85d6"/>
          <stop offset="1" stop-color="#1561b8"/>
        </radialGradient>
      </defs>
      <path d="M640,0 H668 C548,130 492,340 466,580 H440 C470,330 520,120 640,0 Z" fill="var(--green)"/>
      <path d="M0,0 H640 C520,120 470,330 440,580 H0 Z" fill="url(#panelGlow)"/>
    </svg>

    <div class="holder">
      <p class="holder-name">Dorotea Wellmont</p>
      <p class="holder-role">Owner / C.E.O.</p>
    </div>

    <ul class="contact-list">
      <li class="contact-item">
        <span class="contact-icon"><svg viewBox="0 0 24 24"><path d="M12 2a7 7 0 0 0-7 7c0 5 7 13 7 13s7-8 7-13a7 7 0 0 0-7-7zm0 9.5A2.5 2.5 0 1 1 12 6.5a2.5 2.5 0 0 1 0 5z"/></svg></span>
        <span>P.O. Box 2047, Fernvale<br>VIC 3290</span>
      </li>
      <li class="contact-item">
        <span class="contact-icon"><svg viewBox="0 0 24 24"><path d="M6.6 10.8a15 15 0 0 0 6.6 6.6l2.2-2.2c.3-.3.7-.4 1-.2 1.1.4 2.3.6 3.6.6.6 0 1 .4 1 1V20c0 .6-.4 1-1 1A17 17 0 0 1 3 4c0-.6.4-1 1-1h3.5c.6 0 1 .4 1 1 0 1.3.2 2.5.6 3.6.1.3 0 .7-.2 1z"/></svg></span>
        <span>+61 3 5550 1427</span>
      </li>
      <li class="contact-item">
        <span class="contact-icon"><svg viewBox="0 0 24 24"><path d="M6.6 10.8a15 15 0 0 0 6.6 6.6l2.2-2.2c.3-.3.7-.4 1-.2 1.1.4 2.3.6 3.6.6.6 0 1 .4 1 1V20c0 .6-.4 1-1 1A17 17 0 0 1 3 4c0-.6.4-1 1-1h3.5c.6 0 1 .4 1 1 0 1.3.2 2.5.6 3.6.1.3 0 .7-.2 1z"/></svg></span>
        <span>+61 3 5550 1468</span>
      </li>
      <li class="contact-item">
        <span class="contact-icon"><svg viewBox="0 0 24 24"><path d="M2 5h20v14H2zm2 2v.5l8 5 8-5V7z"/></svg></span>
        <span>dpalvane@qzr.example</span>
      </li>
      <li class="contact-item">
        <span class="contact-icon"><svg viewBox="0 0 24 24"><path d="M12 2a10 10 0 1 0 0 20 10 10 0 0 0 0-20zm6.9 6h-3a15 15 0 0 0-1.3-3.9A8 8 0 0 1 18.9 8zM12 4c.8 1.2 1.5 2.5 1.9 4h-3.8c.4-1.5 1.1-2.8 1.9-4zM4.3 14a8 8 0 0 1 0-4h3.4a16 16 0 0 0 0 4zm.8 2h3a15 15 0 0 0 1.3 3.9A8 8 0 0 1 5.1 16zm3-8h-3a8 8 0 0 1 4.3-3.9A15 15 0 0 0 8.1 8zM12 20c-.8-1.2-1.5-2.5-1.9-4h3.8c-.4 1.5-1.1 2.8-1.9 4zm2.3-6H9.7a14 14 0 0 1 0-4h4.6a14 14 0 0 1 0 4zm.3 5.9a15 15 0 0 0 1.3-3.9h3a8 8 0 0 1-4.3 3.9zm1.7-5.9a16 16 0 0 0 0-4h3.4a8 8 0 0 1 0 4z"/></svg></span>
        <span>www.orbworthkeeping.example</span>
      </li>
    </ul>

    <div class="brand">
      <span class="brand-square"></span>
      <span class="brand-name">ORB</span>
    </div>
  </div>
</body>
</html>
```